Melissa Dorvan Personal Business Card

I like orange. It's would better if my card have an orange background
Address: 5820 Halvers Lane #417
San Jose
California
US
Tel: 4085172049

Industry/Entity Type

Business

```html
<!DOCTYPE html>
<html lang="en">
<head>
<meta charset="utf-8">
<title>Melissa Dorvan — Business Card</title>
<link rel="stylesheet" href="https://fonts.googleapis.com/css2?family=Cinzel:wght@400;700;900&display=swap">
<style>
  :root {
    --page-bg: #2a2a2a;
    --tile-yellow: #f7d21a;
    --tile-amber: #f5a515;
    --tile-orange: #e8651c;
    --tile-red: #b8321a;
    --tile-deep: #6e1a0e;
    --band: rgba(40, 24, 12, 0.55);
    --name-silver: #eeeeee;
    --name-shadow: rgba(0, 0, 0, 0.75);
    --detail-text: #ffffff;
  }
  * { box-sizing: border-box; margin: 0; padding: 0; }
  html, body {
    width: 1200px;
    height: 797px;
    overflow: hidden;
    background: var(--page-bg);
  }
  .stage {
    width: 1200px;
    height: 797px;
    display: flex;
    align-items: center;
    justify-content: center;
  }
  .business-card {
    position: relative;
    width: 1040px;
    height: 594px;
    overflow: hidden;
    font-family: "Cinzel", serif;
  }
  .mosaic-background {
    position: absolute;
    inset: 0;
    background:
      radial-gradient(ellipse 55% 60% at 88% 22%, var(--tile-deep) 0%, transparent 70%),
      linear-gradient(215deg, var(--tile-red) 0%, var(--tile-orange) 30%, var(--tile-amber) 55%, var(--tile-yellow) 80%, #fbe66a 100%);
  }
  .card-name {
    position: absolute;
    left: 150px;
    top: 150px;
    font-weight: 700;
    font-size: 92px;
    letter-spacing: 2px;
    font-variant: small-caps;
    color: var(--name-silver);
    text-shadow: 3px 4px 4px var(--name-shadow);
    white-space: nowrap;
  }
  .contact-band {
    position: absolute;
    left: 0;
    right: 0;
    top: 352px;
    height: 130px;
    background: var(--band);
    padding: 22px 40px 0 0;
    text-align: right;
    color: var(--detail-text);
    font-size: 24px;
    line-height: 1.2;
    letter-spacing: 1px;
    font-variant: small-caps;
    text-shadow: 1px 1px 2px rgba(0,0,0,0.6);
  }
  .contact-line { display: block; }
  .contact-line.phone { margin-bottom: 12px; }
</style>
</head>
<body>
  <main class="stage">
    <article class="business-card">
      <div class="mosaic-background" role="img" aria-label="Orange, amber and yellow stained-glass mosaic tile pattern"></div>
      <h1 class="card-name">Melissa Dorvan</h1>
      <address class="contact-band">
        <span class="contact-line phone">Tel: 4085172049</span>
        <span class="contact-line">Address: 5820 Halvers Lane #417</span>
        <span class="contact-line">San Jose California US</span>
      </address>
    </article>
  </main>
</body>
</html>
```